Carrowby Ridge 2013 Vintage Cuvee

We need a label design for a 2013 Vintage Cuvee bottle, which is a premium sparkling white wine.

About Carrowby Ridge Wine (for your information):
Grown in the cool climate GI (Geographical Indicator) of Denmark, WESTERN AUSTRALIA, in the Great Southern the Carrowby Ridge vineyard is located in gravelly loam soil amidst tall Jarrah and Marri trees.

Finished label product must:
• Comply with Australian labelling requirements (see attached shiraz example)
• Fit on the face of standard sparkling wine bottle (exact bottle to be used TBA)
• Use the Carrowby Ridge logo (attached)
• Be clean, modern, and high end design
• See suitable for commercial printing

Please use the attached reserve label as a GUIDE only for your design. Foil closure colour is not determined, designers can use creativity to come up with a stylish new label. the glass colour is green, so this may change your colour scheme choices.

Will provide finalised wording details once we have received the tasting notes from the winemakers but would like to start seeing designs and colour schemes for this

Target Market(s)

Wine drinkers 25-60

Requirements
Must have
• Logo
• Name of wine- 2013 Vintage Cuvee

```html
<!DOCTYPE html>
<html lang="en">
<head>
<meta charset="utf-8">
<title>Carrowby Ridge 2013 Vintage Cuvee – Label Concepts</title>
<link rel="stylesheet" href="https://fonts.googleapis.com/css2?family=Cormorant+Garamond:wght@400;500&display=swap">
<style>
  :root {
    --backdrop: #5b4636;
    --slate: #6e6f6f;
    --slate-ink: #3f4040;
    --slate-type: #f1f1ee;
    --parchment: #e5e0cf;
    --parchment-ink: #5d5d58;
    --onyx: #0c0c0c;
    --onyx-type: #f4f4f2;
  }
  * { box-sizing: border-box; margin: 0; padding: 0; }
  html, body {
    width: 1200px;
    height: 992px;
    overflow: hidden;
    background: var(--backdrop);
  }
  .concepts {
    position: relative;
    width: 1200px;
    height: 992px;
    display: flex;
    justify-content: center;
    align-items: center;
    gap: 60px;
  }
  .label {
    position: relative;
    width: 300px;
    height: 500px;
    font-family: "Cormorant Garamond", serif;
    text-align: center;
  }
  .label-shape {
    position: absolute;
    inset: 0;
    width: 100%;
    height: 100%;
  }
  .label-content {
    position: absolute;
    inset: 0;
    display: flex;
    flex-direction: column;
    align-items: center;
  }
  .brand-name {
    font-weight: 500;
    letter-spacing: 0.04em;
  }
  .vintage-year {
    font-weight: 500;
    letter-spacing: 0.06em;
  }
  .wine-name {
    font-weight: 500;
    line-height: 1;
  }
  .statutory {
    position: absolute;
    left: 0;
    right: 0;
    display: flex;
    justify-content: space-between;
    font-weight: 500;
    font-size: 11px;
    letter-spacing: 0.03em;
  }

  /* Concept 1 – slate */
  .label--slate { background: var(--slate); }
  .label--slate .brand-name { margin-top: 150px; font-size: 30px; color: var(--slate-ink); }
  .label--slate .vintage-year { margin-top: 88px; font-size: 22px; color: var(--slate-type); }
  .label--slate .wine-name { margin-top: 4px; font-size: 30px; color: var(--slate-type); letter-spacing: 0.04em; }
  .label--slate .statutory { bottom: 22px; padding: 0 16px; color: var(--slate-ink); }

  /* Concept 2 – parchment */
  .label--parchment .brand-name { margin-top: 150px; font-size: 30px; color: var(--parchment-ink); }
  .label--parchment .vintage-year { margin-top: 88px; font-size: 24px; color: var(--parchment-ink); }
  .label--parchment .wine-name { margin-top: 2px; font-size: 31px; color: var(--parchment-ink); letter-spacing: 0.06em; text-transform: uppercase; }
  .label--parchment .statutory { bottom: 26px; padding: 0 24px; color: var(--parchment-ink); }

  /* Concept 3 – onyx */
  .label--onyx .brand-name { margin-top: 118px; font-size: 26px; color: var(--onyx-type); }
  .label--onyx .vintage-year { margin-top: 150px; font-size: 14px; color: var(--onyx-type); }
  .label--onyx .wine-name { margin-top: 4px; font-size: 30px; color: var(--onyx-type); letter-spacing: 0.03em; }
  .label--onyx .statutory { bottom: 34px; padding: 0 32px; color: var(--onyx-type); }
</style>
</head>
<body>
<main class="concepts">

  <section class="label label--slate" aria-label="Slate label concept">
    <div class="label-content">
      <p class="brand-name">Carrowby Ridge</p>
      <p class="vintage-year">2013</p>
      <h1 class="wine-name">Vintage Cuvee</h1>
    </div>
    <div class="statutory"><span>750ML</span><span>Alc. 12% By Volume</span></div>
  </section>

  <section class="label label--parchment" aria-label="Parchment label concept">
    <svg class="label-shape" viewBox="0 0 300 500" aria-hidden="true">
      <path d="M16,0 H284 A16,16 0 0 0 300,16 V484 A16,16 0 0 0 284,500 H16 A16,16 0 0 0 0,484 V16 A16,16 0 0 0 16,0 Z" fill="var(--parchment)"/>
    </svg>
    <div class="label-content">
      <p class="brand-name">Carrowby Ridge</p>
      <p class="vintage-year">2013</p>
      <h2 class="wine-name">Vintage Cuvee</h2>
    </div>
    <div class="statutory"><span>750ML</span><span>Alc. 12% By Volume</span></div>
  </section>

  <section class="label label--onyx" aria-label="Onyx label concept">
    <svg class="label-shape" viewBox="0 0 300 500" aria-hidden="true">
      <rect width="300" height="500" fill="var(--onyx)"/>
      <path d="M16,484 V72 H48 Q48,52 68,52 Q150,8 232,52 Q252,52 252,72 H284 V484 Z" fill="none" stroke="var(--onyx-type)" stroke-width="1.5"/>
    </svg>
    <div class="label-content">
      <p class="brand-name">Carrowby Ridge</p>
      <p class="vintage-year">2013</p>
      <h2 class="wine-name">Vintage Cuvee</h2>
    </div>
    <div class="statutory"><span>750 ML</span><span>Alc. 12% By Volume</span></div>
  </section>

</main>
</body>
</html>
```